DORLIT HOMES Professional Home Buyers

Please see two files uploaded. One is my new LOGO (thanks Quenby) and the other gives the wording and pages desired. Of course I am open to suggestions to further enhance what I'm about. I don't want testimonials or houses to buy to appear but to have room for them when I'm ready. I am a real estate investor not a licensed real estate agent. For FAQ i want just the questions to appear and when they click on the question the answer appears and when they click on the question again the answer disappears. make sense? When you read my wording and my idea of pages you'll get an idea of what I'm about. Suggestions are welcomed.

Industry/Entity Type

Real Estate

Number of Pages Required

5+ page

Requirements
Must have
• FAQ pages only questions appear. They click on question the answer appears underneath. they click on question again, the answer disappears. Also, I of course, want my new LOGO to appear on each page I don't know if it will look better all by itself or blended in somehow? Call now 418-555-0193 on each page also. I will get a real phone number before website goes live. If you have a better way of wording what I'm describing please let me know, I am open to feedback
Nice to have
• Anything that the average homeowner can relate to (yea I know, that doesn't help you much, right?)
• Testimonial page and houses to buy page could be done with just the shell ready in the wings for when my business grows it will be ready all that it would need then are the wording and pictures to be uploaded onto the website page. make sense?
Should not have
• I don't want it too elegant or rich looking as I believe my audience will be mostly the average homeowner who needs help

```html
<!DOCTYPE html>
<html lang="en">
<head>
<meta charset="utf-8">
<title>DORLIT HOMES – Professional Home Buyers</title>
<link href="https://fonts.googleapis.com/css2?family=Open+Sans:wght@400;600;700;800&display=swap" rel="stylesheet">
<style>
:root{
  --blue:#1ba4e2;
  --blue-dark:#1287c0;
  --navy:#1e3c5c;
  --nav:#3b3e43;
  --ink:#333a40;
  --muted:#6b7177;
  --band:#e6e7e9;
  --footer:#404448;
  --footer-deep:#2e3134;
  --white:#ffffff;
}
*{box-sizing:border-box;margin:0;padding:0}
html,body{width:822px;height:1200px;overflow:hidden}
body{font-family:"Open Sans",Arial,sans-serif;color:var(--ink);background:var(--white);font-size:10px}
.site-header{height:60px;display:flex;align-items:center;justify-content:space-between;padding:0 44px}
.brand{display:flex;align-items:center;gap:8px;font-weight:800;font-size:19px;color:var(--navy);letter-spacing:.5px}
.brand-mark{width:16px;height:16px;background:var(--navy)}
.header-contacts{display:flex;gap:26px;align-items:center}
.contact-item{display:flex;align-items:center;gap:7px}
.contact-icon{width:22px;height:22px;border-radius:50%;background:var(--blue);display:flex;align-items:center;justify-content:center}
.contact-label{font-size:8px;color:var(--muted);line-height:1}
.contact-value{font-size:14px;font-weight:700;color:var(--navy);line-height:1.1}
.main-nav{height:30px;background:var(--nav);display:flex;align-items:center;justify-content:space-between;padding:0 44px 0 100px}
.nav-links{display:flex;height:100%;list-style:none}
.nav-links li{display:flex;align-items:center;padding:0 14px;color:#e7e8ea;font-size:8.5px;font-weight:600;letter-spacing:.4px}
.nav-links li.active{background:var(--blue);color:var(--white)}
.social{display:flex;gap:4px}
.social span{width:17px;height:17px;display:block}
.s1{background:#3c5a99}.s2{background:#29a9e1}.s3{background:#d44132}
.hero{position:relative;height:295px;background:linear-gradient(180deg,#5f9ed9 0%,#b8d5ee 38%,#eef1f2 55%,#d6d9d6 68%,#2d87c9 82%,#1d5ea0 100%)}
.hero-banner{position:absolute;left:0;top:232px;width:660px;height:36px;background:rgba(20,40,70,.75);display:flex;align-items:center;padding-left:100px;font-size:15px;font-weight:700;color:var(--white);border-left:8px solid var(--blue)}
.hero-banner strong{color:var(--blue);margin-right:6px;font-weight:800}
.welcome{height:190px;text-align:center;padding:26px 100px 0}
.section-title{font-size:17px;font-weight:600;color:var(--ink)}
.section-title em{font-style:normal;color:var(--blue);font-weight:700}
.welcome p{margin:16px 0 18px;font-size:8.5px;line-height:1.6;color:var(--muted)}
.btn{display:inline-block;background:var(--nav);color:var(--white);font-size:7.5px;font-weight:600;letter-spacing:.5px;padding:7px 18px}
.features{height:180px;background:var(--band);display:flex;padding:28px 90px 0;gap:60px}
.feature{flex:1;text-align:center}
.feature h3{font-size:15px;font-weight:700;color:var(--ink)}
.feature p{margin:10px 0 16px;font-size:8px;line-height:1.6;color:var(--muted)}
.btn-outline{background:#d3d5d8;color:var(--ink);border:1px solid #c3c5c8}
.about{height:245px;display:flex;padding:26px 60px 0 90px;gap:40px}
.about-copy{flex:1}
.about-copy h2{font-size:17px;font-weight:700;color:var(--ink);letter-spacing:.3px}
.about-copy h2::after{content:"";display:block;width:34px;height:2px;background:var(--blue);margin-top:4px}
.about-copy p{margin:12px 0 10px;font-size:8px;line-height:1.6;color:var(--muted)}
.bullets{list-style:none}
.bullets li{font-size:8px;line-height:1.9;color:var(--muted);padding-left:11px;position:relative}
.bullets li::before{content:"";position:absolute;left:0;top:6px;width:4px;height:4px;border-radius:50%;background:var(--blue)}
.more-link{display:block;margin-top:8px;color:var(--blue);font-size:8.5px;font-weight:700}
.sell-box{width:222px;height:160px;margin-top:12px;background:var(--blue);padding:14px 18px;color:var(--white)}
.sell-box h3{font-size:15px;font-weight:700;margin-bottom:8px}
.sell-box li{list-style:none;font-size:8px;line-height:2;padding-left:11px;position:relative}
.sell-box li::before{content:"";position:absolute;left:0;top:6px;width:4px;height:4px;background:var(--white)}
.site-footer{height:178px;background:var(--footer);display:flex;padding:26px 44px 0 90px;gap:34px;color:#c9cbcd}
.footer-col h4{font-size:10px;font-weight:700;color:var(--white);margin-bottom:8px}
.footer-col h4::after{content:"";display:block;width:26px;height:2px;background:var(--blue);margin-top:4px}
.links{width:110px}
.links li{list-style:none;font-size:7.5px;line-height:1.85;padding-left:8px;position:relative}
.links li::before{content:"›";position:absolute;left:0;color:var(--blue)}
.newsletter{width:150px}
.newsletter p{font-size:7.5px;line-height:1.6;margin-bottom:10px}
.email-field{height:18px;background:var(--white);color:#9a9ea2;font-size:7px;padding:4px 7px;margin-bottom:6px}
.submit{display:inline-block;background:var(--blue);color:var(--white);font-size:7px;font-weight:700;padding:4px 10px}
.contact-detail{width:150px}
.contact-detail dt{font-size:7px;font-weight:700;color:var(--white);margin-top:4px}
.contact-detail dd{font-size:7.5px;line-height:1.5}
.footer-brand{margin-left:auto;align-self:center;display:flex;align-items:center;gap:7px;font-weight:800;font-size:18px;color:#7e8388;margin-top:-20px}
.footer-brand span{width:14px;height:14px;background:#7e8388;display:block}
.copyright{height:22px;background:var(--footer-deep);color:#9ea2a6;font-size:7px;display:flex;align-items:center;justify-content:center}
</style>
</head>
<body>
<header class="site-header">
  <div class="brand"><span class="brand-mark"></span>DORLIT HOMES</div>
  <div class="header-contacts">
    <div class="contact-item">
      <span class="contact-icon"><svg width="11" height="11" viewBox="0 0 24 24"><path fill="#fff" d="M6.6 10.8a15 15 0 0 0 6.6 6.6l2.2-2.2c.3-.3.7-.4 1-.2 1.1.4 2.3.6 3.6.6.6 0 1 .4 1 1V20c0 .6-.4 1-1 1A17 17 0 0 1 3 4c0-.6.4-1 1-1h3.5c.6 0 1 .4 1 1 0 1.3.2 2.5.6 3.6.1.3 0 .7-.2 1z"/></svg></span>
      <div><div class="contact-label">Call us</div><div class="contact-value">418-555-0193</div></div>
    </div>
    <div class="contact-item">
      <span class="contact-icon"><svg width="11" height="11" viewBox="0 0 24 24"><path fill="#fff" d="M2 5h20v14H2z"/><path fill="none" stroke="#1ba4e2" stroke-width="2" d="M2 6l10 7 10-7"/></svg></span>
      <div><div class="contact-label">Email</div><div class="contact-value">info@dorlithomes.com</div></div>
    </div>
  </div>
</header>

<nav class="main-nav">
  <ul class="nav-links">
    <li class="active">HOME</li><li>ABOUT US</li><li>FAQ</li><li>CONTACT US</li><li>TESTIMONIALS</li><li>HOUSES TO BUY</li>
  </ul>
  <div class="social"><span class="s1"></span><span class="s2"></span><span class="s3"></span></div>
</nav>

<section class="hero" role="img" aria-label="Photo of a bright white modern house with palm trees and a blue swimming pool">
  <div class="hero-banner"><strong>DORLIT HOMES</strong> Will Buy Your House AS IS, FAST &amp; HASSLE</div>
</section>

<section class="welcome">
  <h1 class="section-title">Welcome to <em>DORLIT HOMES</em></h1>
  <p>Selling a house should not be a long, stressful ordeal. We are local home buyers who make fair cash offers on houses in any condition, in any area, at any price. There are no agent fees, no repairs to make and no cleaning to do. You choose the closing date that suits you and we handle every step so you can move on with less worry and more time.</p>
  <span class="btn">Read More</span>
</section>

<section class="features">
  <div class="feature">
    <h3>We buy houses in any condition!</h3>
    <p>Don't want to spend money on repairs? DORLIT HOMES buys houses as they stand, from fire damage to outdated kitchens. Tell us about your place and we will make a fair offer quickly.</p>
    <span class="btn btn-outline">GET YOUR FREE QUOTE</span>
  </div>
  <div class="feature">
    <h3>Get cash for your house!</h3>
    <p>We pay cash and can close in as little as seven days. No banks, no showings and no waiting on buyer financing. Get your offer and decide on your own schedule.</p>
    <span class="btn btn-outline">GET MORE INFO</span>
  </div>
</section>

<section class="about">
  <div class="about-copy">
    <h2>ABOUT US</h2>
    <p>DORLIT HOMES buys houses quickly in any price range, in any condition. We have helped people just like you in all kinds of situations:</p>
    <ul class="bullets">
      <li>You can't afford expensive repairs</li>
      <li>You inherited another home</li>
      <li>You are dealing with a divorce</li>
      <li>You are behind on payments</li>
      <li>You have fallen behind on taxes</li>
    </ul>
    <span class="more-link">GET MORE INFO</span>
  </div>
  <aside class="sell-box">
    <h3>Sell Your Home FAST!</h3>
    <ul>
      <li>We pay all cash</li>
      <li>We pay most closing costs</li>
      <li>We buy as is</li>
      <li>No waiting for bank approvals</li>
      <li>Close on your schedule</li>
    </ul>
  </aside>
</section>

<footer class="site-footer">
  <div class="footer-col links">
    <h4>Quick Links</h4>
    <ul><li>Home</li><li>About Us</li><li>Houses To Buy</li><li>FAQ</li><li>Testimonials</li><li>Contact Us</li></ul>
  </div>
  <div class="footer-col newsletter">
    <h4>Newsletter</h4>
    <p>Simply sign up to get tips for selling your home fast.</p>
    <div class="email-field">Enter Email</div>
    <span class="submit">SUBMIT</span>
  </div>
  <div class="footer-col contact-detail">
    <h4>Contact Detail</h4>
    <dl>
      <dt>Phone</dt><dd>418-555-0193</dd>
      <dt>Address</dt><dd>Your Street Address, City, State</dd>
      <dt>Email</dt><dd>info@dorlithomes.com</dd>
    </dl>
  </div>
  <div class="footer-brand"><span></span>DORLIT HOMES</div>
</footer>
<div class="copyright">Copyright © 2024 DorlitHomes.com | All Rights Reserved</div>
</body>
</html>
```